Logo and Flyer design Layerix Expo 2019

A logo and flyer design for a 3D Medical printing conference to be held in Melbourne Australia. The conference audience is aimed at people who have an interesting in 3D printing to benefit their work as well as printing for a hobby. Mostly professionals in the medical, bio-engineering, VET sciences fields who are 3D printing models for patients and simulation will attend this conference.

Target Market(s)

medical, bio-engineering, VET sciences fields who are 3D printing models for patients and simulation will attend this conference.

Industry/Entity Type

Medical And Science

Font styles to use
Sans Serif

Colors
3276b5
e34197
fbee3d
f68d4c
f04a50

Requirements
Must have
• Layerix logo
• Jaw
• Futuristic theme
• Layerix colours
Nice to have
• Unique design
Should not have
• Pictures from lookfar pics

```html
<!DOCTYPE html>
<html lang="en">
<head>
<meta charset="utf-8">
<title>Layerix Australia Conference 2019</title>
<link rel="stylesheet" href="https://fonts.googleapis.com/css2?family=Aldrich&display=swap">
<style>
  :root {
    --blue: #3276b5;
    --blue-deep: #2a62a0;
    --blue-light: #5a9fd6;
    --pink: #e34197;
    --yellow: #fbee3d;
    --orange: #f68d4c;
    --white: #ffffff;
    --bone: #d9b24a;
  }
  html, body {
    margin: 0;
    padding: 0;
    overflow: hidden;
    background: #ffffff;
  }
  .flyer {
    position: relative;
    width: 927px;
    height: 1200px;
    overflow: hidden;
    font-family: "Aldrich", sans-serif;
    background: var(--blue-deep);
  }
  .backdrop {
    position: absolute;
    left: 0; top: 0;
    width: 855px; height: 1200px;
    background:
      radial-gradient(ellipse 180px 260px at 470px 470px, rgba(150,210,255,0.55), rgba(150,210,255,0) 70%),
      linear-gradient(180deg, #2f6caa 0%, #3a7cbc 35%, #3b7fbf 55%, #4a86bf 80%, #4e86b8 100%);
  }
  .accent-bar {
    position: absolute;
    right: 0; top: 0;
    width: 72px; height: 1200px;
    background: var(--yellow);
  }
  .logo-field {
    position: absolute;
    left: 0; top: 0;
    width: 358px; height: 335px;
    background: radial-gradient(circle at 50% 50%, #5c90c6 0%, #4a83bd 60%, #3f78b3 100%);
  }
  .logo-name {
    position: absolute;
    left: 0; top: 140px;
    width: 358px;
    text-align: center;
    font-size: 46px;
    color: var(--orange);
    letter-spacing: 1px;
  }
  .eyebrow {
    position: absolute;
    right: 94px; top: 74px;
    width: 480px;
    text-align: right;
    color: var(--pink);
    font-size: 36px;
    line-height: 67px;
    letter-spacing: 4px;
    text-transform: uppercase;
  }
  .title {
    position: absolute;
    right: 94px; top: 332px;
    text-align: right;
    color: var(--white);
    font-size: 52px;
    line-height: 68px;
    letter-spacing: 1px;
    text-transform: uppercase;
    margin: 0;
    font-weight: 400;
  }
  .location {
    position: absolute;
    right: 94px; top: 518px;
    text-align: right;
    color: var(--white);
    font-size: 22px;
    margin: 0;
  }
  .dates {
    position: absolute;
    right: 110px; top: 548px;
    text-align: right;
    color: var(--white);
    font-size: 16px;
    letter-spacing: 3px;
    margin: 0;
  }
  .about {
    position: absolute;
    right: 111px; top: 640px;
    text-align: right;
    color: var(--white);
    font-size: 21px;
    line-height: 40px;
    margin: 0;
  }
  .jaw-photo {
    position: absolute;
    left: 0; top: 960px;
    width: 239px; height: 240px;
    background: linear-gradient(160deg, #f2f2f0 0%, #e4e2dc 55%, #c9b27a 100%);
  }
</style>
</head>
<body>
  <main class="flyer">
    <div class="backdrop" role="img" aria-label="Blue futuristic data corridor background"></div>
    <div class="accent-bar"></div>

    <div class="logo-field" role="img" aria-label="Circuit-board decoration around the Layerix name"></div>
    <div class="logo-name">Layerix</div>

    <p class="eyebrow" style="margin:0">The Layerix Lab is hosting its 5th annual</p>

    <h1 class="title">Layerix Australia<br>Conference</h1>

    <p class="location">in Melbourne, Australia</p>
    <p class="dates">NOVEMBER 14-16, 2019</p>

    <p class="about">
      The conference audience is aimed at<br>
      people who have an interesting in<br>
      3D printing to benefit their work as<br>
      well as printing for a hobby. Mostly<br>
      professionals in the medical,<br>
      bioengineering, VET sciences fields<br>
      who are 3D printing models for<br>
      patients and simulation will attend<br>
      this conference.<br>
      This year the conference will bring<br>
      international and interstate<br>
      speakers
    </p>

    <div class="jaw-photo" role="img" aria-label="Photo of a 3D printed translucent yellow jaw model"></div>
  </main>
</body>
</html>
```